Yoga class opening. Little schedule for JUNE JULY and AUGUST

Flyer to promote an opening yoga class. The color of the docx haven't to be respected.

We want something joyfull, professional, clean and serious.

About the logo we oppened a contest at the same time so at the moment there is no logo but the logo color will be simple.

The phone number will change so you can poste a random one for the design that i can change by myself.

i recieved many creation in both side BUT i want something in 1 side :)

Target Market(s)

Yoga student. all age

Industry/Entity Type

It Professional

Logo Text

Yoga fern

Font styles to use
Sans Serif

Requirements
Must have
• The text present on the docx
Nice to have
• Some symbols about yoga ( Namasté signs, mandala, ... )
Should not have
• Not too much details it has to be clear.

```html
<!DOCTYPE html>
<html lang="fr">
<head>
<meta charset="utf-8">
<title>Yoga fern – stages et ateliers d'été</title>
<link rel="stylesheet" href="https://fonts.googleapis.com/css2?family=Montserrat:wght@300;400;500;600;700&display=swap">
<style>
  :root {
    --orange: #f07f1e;
    --orange-deep: #f08a2c;
    --ink: #2f2f2f;
    --paper: #ffffff;
    --mist: #dedcdb;
    --ornament: rgba(240, 127, 30, 0.16);
  }
  * { margin: 0; padding: 0; box-sizing: border-box; }
  html, body { width: 846px; height: 1200px; overflow: hidden; }
  body { font-family: "Montserrat", sans-serif; color: var(--ink); }

  .flyer {
    position: relative;
    width: 846px;
    height: 1200px;
    overflow: hidden;
    background: linear-gradient(180deg, var(--paper) 0%, #f3f2f2 14%, var(--mist) 38%, #ecc9a5 58%, #f4a760 76%, var(--orange-deep) 100%);
  }
  .ornaments { position: absolute; inset: 0; width: 846px; height: 1200px; }

  .abs { position: absolute; }
  .opening { left: 55px; top: 38px; font-size: 25px; font-weight: 700; color: var(--orange); line-height: 1; }
  .address { left: 55px; top: 66px; font-size: 17.5px; color: var(--orange); line-height: 24px; text-transform: uppercase; }
  .intro { left: 55px; top: 140px; font-size: 15px; line-height: 24px; }

  .brand { right: 56px; top: 34px; text-align: right; }
  .brand-name { font-size: 41px; font-weight: 700; color: var(--orange); line-height: 1; letter-spacing: 0.5px; }
  .brand-tag { font-size: 11.5px; font-weight: 700; color: var(--orange); margin-top: 16px; }
  .brand-new { font-size: 35px; font-weight: 300; color: var(--orange); margin-top: 6px; line-height: 1; }

  .month { font-size: 36px; font-weight: 700; line-height: 1; text-transform: uppercase; }
  .offer { font-size: 20.5px; font-weight: 600; line-height: 28px; text-transform: uppercase; }
  .price { font-size: 20.5px; font-weight: 400; line-height: 1; }
  .price strong { font-weight: 700; }

  .sessions { list-style: none; }
  .sessions li { display: block; }
  .sessions .when { display: block; font-size: 15.5px; font-weight: 700; line-height: 26.4px; }
  .sessions .when sup { font-size: 9px; }
  .sessions .hours { display: block; font-size: 13px; font-weight: 400; line-height: 26.4px; }
  .workshops { list-style: none; }
  .workshops li { font-size: 15.5px; font-weight: 700; line-height: 26.4px; }
  .workshops li span { font-size: 13px; font-weight: 400; }

  .note { left: 454px; top: 955px; font-size: 11px; }
  .closing { right: 55px; top: 1062px; text-align: right; }
  .closing p { font-size: 17px; line-height: 24px; }
  .closing .wish { font-size: 22px; font-weight: 700; line-height: 1; margin-top: 8px; }
</style>
</head>
<body>
<main class="flyer">
  <svg class="ornaments" viewBox="0 0 846 1200" role="img" aria-label="Décor de mandalas orange en filigrane">
    <circle cx="732" cy="-12" r="290" fill="none" stroke="var(--ornament)" stroke-width="46"/>
    <circle cx="732" cy="-12" r="226" fill="rgba(255,255,255,0.35)"/>
    <circle cx="790" cy="720" r="320" fill="var(--ornament)"/>
    <circle cx="0" cy="760" r="150" fill="var(--ornament)"/>
    <circle cx="80" cy="1110" r="180" fill="rgba(255,255,255,0.08)"/>
  </svg>

  <div class="abs opening">OUVERTURE LE 6 JUIN 2016</div>
  <div class="abs address">Au 112 Rue des Lilas<br>1050 Ixelles</div>
  <p class="abs intro">En attendant le planning des cours de la rentrée,<br>YOGA FERN vous propose ses stages et ateliers d’été.</p>

  <header class="abs brand">
    <div class="brand-name">YOGA FERN</div>
    <div class="brand-tag">VOTRE STUDIO DE YOGA A IXELLES</div>
    <div class="brand-new">NOUVEAU !!</div>
  </header>

  <!-- Juin -->
  <h2 class="abs month" style="left:55px; top:208px;">Juin</h2>
  <h3 class="abs offer" style="left:55px; top:247px;">Stage découverte du yoga</h3>
  <div class="abs price" style="left:55px; top:283px;">10H00 <strong>85 €</strong></div>
  <ul class="abs sessions" style="left:55px; top:343px;">
    <li><span class="when">DU LUNDI 6 AU VENDREDI 10 JUIN</span><span class="hours">10H00 À 12H00 OU 18H00 À 20H00</span></li>
    <li><span class="when">DU LUNDI 13 AU VENDREDI 17 JUIN</span><span class="hours">10H00 À 12H00 OU 18H00 À 20H00</span></li>
    <li><span class="when">DU LUNDI 20 AU VENDREDI 24 JUIN</span><span class="hours">10H00 À 12H00 OU 18H00 À 20H00</span></li>
    <li><span class="when">DU LUNDI 27 AU VENDREDI 1<sup>ER</sup> JUILLET</span><span class="hours">10H00 À 12H00 OU 18H00 À 20H00</span></li>
  </ul>

  <h3 class="abs offer" style="left:55px; top:581px;">Atelier gestion du stress<br>Yoga/&nbsp; sophrologie</h3>
  <div class="abs price" style="left:55px; top:636px;">2H00 <strong>28 €</strong></div>
  <ul class="abs workshops" style="left:55px; top:686px;">
    <li>SAMEDI 11 JUIN <span>10H30 À 12H30</span></li>
    <li>SAMEDI 11 JUIN <span>15H À 17H00</span></li>
    <li>DIMANCHE 12 JUIN <span>10H30 À 12H30</span></li>
    <li>DIMANCHE 12 JUIN <span>14H À 16H00</span></li>
  </ul>

  <!-- Juillet -->
  <h2 class="abs month" style="left:55px; top:808px;">Juillet</h2>
  <h3 class="abs offer" style="left:55px; top:850px;">Stage initiation à l’ashtanga</h3>
  <div class="abs price" style="left:55px; top:884px;">10H00 <strong>85 €</strong></div>
  <ul class="abs sessions" style="left:55px; top:942px;">
    <li><span class="when">DU LUNDI 4 AU VENDREDI 8 JUILLET</span><span class="hours">10H00 À 12H00 OU 18H00 À 20H00</span></li>
    <li><span class="when">DU LUNDI 11 AU VENDREDI 15 JUILLET</span><span class="hours">10H00 À 12H00 OU 18H00 À 20H00</span></li>
    <li><span class="when">DU LUNDI 18 AU VENDREDI 22 JUILLET</span><span class="hours">10H00 À 12H00 OU 18H00 À 20H00</span></li>
    <li><span class="when">DU LUNDI 25 AU VENDREDI 29 JUILLET</span></li>
  </ul>

  <h3 class="abs offer" style="left:454px; top:340px;">Atelier gestion du stress<br>Yoga/sophrologie</h3>
  <div class="abs price" style="left:454px; top:395px;">2H00 <strong>28 €</strong></div>
  <ul class="abs workshops" style="left:454px; top:440px;">
    <li>SAMEDI 9 JUILLET <span>10H30 À 12H30</span></li>
    <li>SAMEDI 9 JUILLET <span>15H00 À 17H00</span></li>
    <li>DIMANCHE 10 JUILLET <span>10H30 À 12H30</span></li>
    <li>DIMANCHE 10 JUILLET <span>14H00 À 16H00</span></li>
  </ul>

  <!-- Août -->
  <h2 class="abs month" style="left:454px; top:572px;">Aout</h2>
  <h3 class="abs offer" style="left:454px; top:614px;">Stage découverte du yoga</h3>
  <div class="abs price" style="left:454px; top:649px;">10H00 <strong>85 €</strong></div>
  <ul class="abs sessions" style="left:454px; top:706px;">
    <li><span class="when">DU LUNDI 1ER AU VENDREDI 5 AOÛT</span><span class="hours">10H00 À 12H00 OU 18H00 À 20H00</span></li>
    <li><span class="when">DU LUNDI 8 AU VENDREDI 12 AOÛT</span><span class="hours">10H00 À 12H00 OU 18H00 À 20H00</span></li>
    <li><span class="when">DU LUNDI 15 AU VENDREDI 19 AOÛT</span><span class="hours">10H00 À 12H00 OU 18H00 À 20H00</span></li>
    <li><span class="when">DU LUNDI 22 AU VENDREDI 26 AOÛT</span><span class="hours">10H00 À 12H00 OU 18H00 À 20H00</span></li>
  </ul>

  <p class="abs note">Démarrage du planning annuel le 5 septembre 2016</p>

  <footer class="abs closing">
    <p>Plus d’info et inscription</p>
    <p>Ou via notre page Sociala : yoga fern</p>
    <p class="wish">UN BEL ETE A TOUS !</p>
  </footer>
</main>
</body>
</html>
```